Innovative Consulting Firm Needs New Business Cards and Stationary

Our Innovative Consulting Firm, Larkfield Consulting, is in need of new business cards and stationary designs. We want two-sided cards that incorporate our logo, which is attached. We are looking for something not too formal, but is professional and slick.

Card should have the following information:
Name (ex. Tom Bradley)
Title (ex. Manager)
Address (ex. 24680 Cedar Lane)
Address 2 (ex. Suite 100)
City
State
Zip Code
Mobile
Email

The card should also have our website: www.larkfieldconsulting.example

Industry/Entity Type

Management Consulting

Contact Information for Business Card

Name (ex. Tom Bradley)
Title (ex. Manager)
Address 2 (ex. Suite 100)
City
State
Zip Code
Mobile
Email

Font styles to use
Sans Serif

Requirements
Must have
• The colors on the card must match the colors in the logo. The exact color codes are attached in a pdf.
Nice to have
• The Company's Tagline is "Focused on your Future". This might be nice to incorporate, but not necessary.

```html
<!DOCTYPE html>
<html lang="en">
<head>
<meta charset="utf-8">
<title>Larkfield Consulting – Business Cards</title>
<link rel="stylesheet" href="https://fonts.googleapis.com/css2?family=Michroma&family=Montserrat:wght@400;500;600&display=swap">
<style>
  :root {
    --brand-blue: #1d5283;
    --brand-orange: #f3b21b;
    --paper: #ffffff;
    --backdrop: #e9ebee;
    --text-light: #ffffff;
  }
  * { box-sizing: border-box; margin: 0; padding: 0; }
  html, body { width: 1200px; height: 900px; overflow: hidden; }
  body {
    background: var(--backdrop);
    font-family: "Montserrat", sans-serif;
    display: flex;
    flex-direction: column;
    align-items: center;
    justify-content: center;
    gap: 56px;
  }
  .card {
    position: relative;
    width: 620px;
    height: 354px;
    border-radius: 22px;
    overflow: hidden;
    box-shadow: 0 10px 28px rgba(0,0,0,0.18);
  }

  /* Logo side */
  .card-front { background: var(--brand-blue); }
  .card-front .wordmark {
    position: absolute;
    left: 0; right: 0; top: 128px;
    text-align: center;
    color: var(--text-light);
  }
  .wordmark-name {
    font-family: "Montserrat", sans-serif;
    font-weight: 600;
    font-size: 40px;
    letter-spacing: 1px;
    white-space: nowrap;
  }
  .card-front .website {
    position: absolute;
    left: 0; right: 0; bottom: 36px;
    display: flex;
    justify-content: center;
    align-items: center;
    gap: 8px;
    color: var(--text-light);
    font-size: 15px;
    font-weight: 500;
  }
  .dot { width: 6px; height: 6px; border-radius: 50%; background: var(--brand-orange); }

  /* Details side */
  .card-back { background: var(--paper); }
  .card-back .swoosh { position: absolute; inset: 0; }
  .card-back .wordmark {
    position: absolute;
    left: 36px; top: 112px;
    color: var(--brand-blue);
  }
  .card-back .wordmark-name { font-size: 26px; letter-spacing: 0.5px; }
  .tagline {
    position: absolute;
    left: 36px; top: 190px;
    font-family: "Michroma", sans-serif;
    font-size: 12px;
    color: var(--brand-blue);
    letter-spacing: 0.3px;
    white-space: nowrap;
  }
  .contact {
    position: absolute;
    right: 24px; top: 90px;
    text-align: right;
    color: var(--text-light);
  }
  .person-name {
    font-size: 20px;
    font-weight: 600;
    color: var(--brand-orange);
    letter-spacing: 0.5px;
    line-height: 24px;
  }
  .person-title { font-size: 12px; margin-bottom: 12px; }
  .contact-list { list-style: none; font-size: 12px; line-height: 20px; }
  .contact-list li { display: flex; justify-content: flex-end; align-items: center; gap: 7px; white-space: nowrap; }
  .contact-list svg { width: 10px; height: 10px; flex: none; }
</style>
</head>
<body>

  <section class="card card-front" aria-label="Card front">
    <div class="wordmark"><span class="wordmark-name">Larkfield Consulting</span></div>
    <div class="website"><span class="dot"></span>www.larkfieldconsulting.example<span class="dot"></span></div>
  </section>

  <section class="card card-back" aria-label="Card back">
    <svg class="swoosh" viewBox="0 0 620 354" aria-hidden="true">
      <path d="M400 0 C390 140 320 280 180 354 L620 354 L620 0 Z" fill="var(--brand-blue)"/>
      <path d="M385 20 C370 160 300 300 140 336 L140 348 C320 322 392 170 385 20 Z" fill="var(--brand-orange)"/>
    </svg>

    <div class="wordmark"><span class="wordmark-name">Larkfield Consulting</span></div>
    <p class="tagline">FOCUSED ON YOUR FUTURE</p>

    <div class="contact">
      <p class="person-name">TOM BRADLEY</p>
      <p class="person-title">Manager</p>
      <ul class="contact-list">
        <li>+330 5550-1234
          <svg viewBox="0 0 12 12"><rect x="3" y="0.5" width="6" height="11" rx="1.2" fill="none" stroke="var(--brand-orange)" stroke-width="1.3"/><circle cx="6" cy="9.5" r="0.8" fill="var(--brand-orange)"/></svg>
        </li>
        <li>info@larkfieldconsulting.example
          <svg viewBox="0 0 12 12"><rect x="0.7" y="2" width="10.6" height="8" fill="none" stroke="var(--brand-orange)" stroke-width="1.2"/><path d="M1 2.5 L6 6.5 L11 2.5" fill="none" stroke="var(--brand-orange)" stroke-width="1.2"/></svg>
        </li>
        <li>www.larkfieldconsulting.example
          <svg viewBox="0 0 12 12"><circle cx="6" cy="6" r="5" fill="none" stroke="var(--brand-orange)" stroke-width="1.2"/><path d="M1 6 H11 M6 1 C3 4 3 8 6 11 M6 1 C9 4 9 8 6 11" fill="none" stroke="var(--brand-orange)" stroke-width="1"/></svg>
        </li>
        <li>24680 Cedar Lane Suite 100
          <svg viewBox="0 0 12 12"><path d="M6 11.5 C2.5 7 2 5.5 2 4.5 A4 4 0 0 1 10 4.5 C10 5.5 9.5 7 6 11.5 Z" fill="var(--brand-orange)"/><circle cx="6" cy="4.5" r="1.4" fill="var(--brand-blue)"/></svg>
        </li>
      </ul>
    </div>
  </section>

</body>
</html>
```